Fabrication and machining company needing printed material designs.

Heron Vessels, Inc. wants to use appealing visuals as well as informative text to tell potential clients about our capabilities in fabrication and machining. We have a new logo to showcase as well as a new website. The use of print media will allow us to leave tangible information with clients, and therefore the design will need to be concise, informative, and visually appealing.

Full Page Flyer (approx. 8.5" x 11"), front and back design. This will be a detailed offering of capabilities and services for our shop.

Half Page Flyer (approx. 5.5" x 8.5"), front and back design. An abbreviated version of the full page flyer, meant to be easily handed out and stored inside a note book.

Bi-fold business card front and back. General offerings of our services. Minimal if any details. Finished size is twice the size of a business card (approx. 4" x 3.5"), once folded in half will be the same size as a standard business card (approx. 2" x 3.5").

Please use www.heronvesselsinc.example for theme ideas. The font used for our logo is ethnocentric, not to be used for all text.

Target Market(s)

Industrial Consumers

Font styles to use
Sans Serif

```html
<!DOCTYPE html>
<html lang="en">
<head>
<meta charset="utf-8">
<title>Heron Vessels, Inc. — Capabilities Flyer</title>
<link href="https://fonts.googleapis.com/css2?family=Michroma&family=Roboto:wght@400;500&display=swap" rel="stylesheet">
<style>
  :root {
    --orange: #ee7d2b;
    --brown: #4a2410;
    --charcoal: #4a4a4a;
    --panel: #383838;
    --light: #e4e4e4;
    --white: #ffffff;
    --page: #ffffff;
  }
  * { margin: 0; padding: 0; box-sizing: border-box; }
  html, body { width: 1200px; height: 1200px; overflow: hidden; background: var(--page); }
  .flyer {
    position: absolute; left: 194px; top: 54px;
    width: 812px; height: 1062px;
    background: var(--light);
    overflow: hidden;
    border-radius: 6px 6px 0 0;
    font-family: "Roboto", sans-serif;
  }
  .hero-art {
    position: absolute; left: 0; top: 0; width: 812px; height: 626px;
    background: linear-gradient(160deg, #ececec 0%, #dedede 55%, #cfcfcf 100%);
  }
  .hero-shapes { position: absolute; left: 0; top: 0; }
  .intro {
    position: absolute; left: 35px; top: 26px; width: 240px;
    font-family: "Michroma", sans-serif; font-size: 11.5px; line-height: 16.5px;
    color: var(--orange); text-transform: uppercase; letter-spacing: 1px;
  }
  .wordmark { position: absolute; left: 2px; top: 340px; }
  .services {
    position: absolute; list-style: none;
    font-family: "Michroma", sans-serif; font-size: 13px; letter-spacing: 3px;
    color: var(--orange); text-transform: uppercase;
  }
  .services li { height: 19.5px; line-height: 19.5px; position: relative; padding-left: 14px; }
  .services li::before {
    content: ""; position: absolute; left: 0; top: 6px;
    width: 9px; height: 9px; border-radius: 50%; background: #000;
  }
  .services--left { left: 54px; top: 476px; }
  .services--right { left: 558px; top: 476px; }
  .industries {
    position: absolute; left: 0; top: 626px; width: 812px; height: 368px;
    background: var(--panel);
  }
  .industries__title {
    position: absolute; left: 0; width: 812px; top: 18px; text-align: center;
    font-family: "Michroma", sans-serif; font-size: 20px; color: var(--white); letter-spacing: 1px;
  }
  .industries__rule { position: absolute; left: 382px; top: 47px; width: 48px; height: 2px; background: var(--orange); }
  .industries__map { position: absolute; left: 0; top: 0; }
  .industry-label {
    position: absolute; font-family: "Roboto", sans-serif; font-weight: 500;
    font-size: 13px; color: var(--white); white-space: nowrap; transform: translateX(-50%);
  }
  .contact-bar {
    position: absolute; left: 0; top: 994px; width: 812px; height: 56px;
    border-top: 6px solid var(--orange); border-bottom: 7px solid var(--orange);
    background: var(--brown); display: flex;
  }
  .contact-item {
    width: 204px; display: flex; align-items: center; gap: 6px; padding-left: 12px;
    color: var(--orange); font-size: 10.5px; border-right: 1px solid #2c150a;
  }
  .contact-item:nth-child(3) { width: 204px; border-right: none; }
  .contact-item:last-child { border-right: none; padding-left: 24px; }
  .contact-item svg { flex: none; }
  .flyer-foot { position: absolute; left: 0; top: 1050px; width: 812px; height: 12px; background: #e2e2e2; }
</style>
</head>
<body>
<main class="flyer">
  <div class="hero-art" role="img" aria-label="Faint rendered illustration of storage tanks and a horizontal vessel"></div>

  <svg class="hero-shapes" width="812" height="626" viewBox="0 0 812 626">
    <polygon points="2,0 293,0 318,152 109,306 2,306" fill="var(--charcoal)"/>
    <polygon points="370,0 812,0 812,260 700,218 680,182" fill="var(--charcoal)"/>
    <polygon points="342,0 370,0 680,182 700,218 812,260 812,282 694,232 674,196" fill="var(--brown)"/>
    <polygon points="342,0 356,0 666,196 686,230 812,282 812,298 678,240 658,206" fill="var(--orange)"/>
    <polygon points="548,206 580,198 634,254" fill="var(--charcoal)"/>
  </svg>

  <p class="intro">Heron Vessels Inc. is a leading tank manufacturer located in Rocky Mountain region. We specialize in API-12F &amp; API-650 tank manufacturing serving Utah, Colorado, Wyoming, and North Dakota.</p>

  <svg class="wordmark" width="810" height="170" viewBox="0 0 810 170">
    <text x="0" y="60" textLength="808" lengthAdjust="spacingAndGlyphs" font-family="Michroma, sans-serif" font-size="66" fill="var(--charcoal)">HERON VESSELS</text>
    <text x="155" y="97" textLength="490" lengthAdjust="spacingAndGlyphs" font-family="Michroma, sans-serif" font-size="21" fill="var(--orange)" letter-spacing="4">WWW.HERONVESSELSINC.EXAMPLE</text>
    <text x="720" y="102" textLength="88" lengthAdjust="spacingAndGlyphs" font-family="Michroma, sans-serif" font-size="30" fill="var(--charcoal)">INC.</text>
  </svg>

  <ul class="services services--left">
    <li>Oil production tanks &amp; accessories</li>
    <li>API 12-F, API 650 specification built</li>
    <li>Tanks</li>
    <li>Fire tubes</li>
    <li>Tank heaters</li>
  </ul>
  <ul class="services services--right">
    <li>Tank coils</li>
    <li>Walkways</li>
    <li>Stairs</li>
    <li>Pump skids</li>
  </ul>

  <section class="industries">
    <h2 class="industries__title">INDUSTRIES SERVED</h2>
    <div class="industries__rule"></div>
    <svg class="industries__map" width="812" height="368" viewBox="0 626 812 368">
      <path d="M257 723 Q262 860 405 917 Q548 860 557 723" fill="none" stroke="var(--white)" stroke-width="2.5" stroke-dasharray="0.1 9" stroke-linecap="round"/>
      <rect x="299" y="730" width="216" height="84" rx="3" fill="url(#plantFill)" role="img" aria-label="Photo of a tank battery with stairs and walkway"/>
      <defs>
        <linearGradient id="plantFill" x1="0" y1="0" x2="0" y2="1">
          <stop offset="0" stop-color="#4c4c4a"/>
          <stop offset="0.5" stop-color="#bdb8a8"/>
          <stop offset="1" stop-color="#6d6a62"/>
        </linearGradient>
      </defs>
      <text x="405" y="851" text-anchor="middle" font-family="Michroma, sans-serif" font-size="17" fill="var(--white)">HERON VESSELS</text>
      <g fill="var(--orange)" stroke="var(--white)" stroke-width="3">
        <circle cx="257" cy="723" r="7"/>
        <circle cx="286" cy="858" r="7"/>
        <circle cx="405" cy="917" r="7"/>
        <circle cx="528" cy="858" r="7"/>
        <circle cx="557" cy="723" r="7"/>
      </g>
      <g fill="none" stroke="var(--white)" stroke-width="1.5">
        <circle cx="225" cy="728" r="14"/>
        <path d="M217 736 h16 M220 736 l5 -14 l5 14 M216 726 l14 -4"/>
        <circle cx="257" cy="870" r="14"/>
        <path d="M248 874 h18 v-6 h-18 z M257 868 v-6 M253 862 h8"/>
        <circle cx="407" cy="952" r="14"/>
        <path d="M399 944 l16 16 M415 944 l-16 16"/>
        <circle cx="557" cy="868" r="14"/>
        <path d="M549 876 h16 l-6 -12 h-4 z"/>
        <circle cx="589" cy="728" r="14"/>
        <path d="M589 728 v10 M589 728 l-7 -6 M589 728 l8 -3 M589 728 l-1 9"/>
      </g>
    </svg>
    <span class="industry-label" style="left:214px; top:125px;">Oil &amp; Gas</span>
    <span class="industry-label" style="left:211px; top:265px;">Water &amp; Waste Water</span>
    <span class="industry-label" style="left:407px; top:349px;">Mining</span>
    <span class="industry-label" style="left:572px; top:265px;">Aggregate</span>
    <span class="industry-label" style="left:626px; top:125px;">Power Generation</span>
  </section>

  <footer class="contact-bar">
    <div class="contact-item">
      <svg width="30" height="30" viewBox="0 0 30 30"><circle cx="15" cy="15" r="14" fill="none" stroke="var(--orange)" stroke-width="1.5"/><path d="M15 8 a5 5 0 0 1 5 5 c0 4 -5 9 -5 9 s-5 -5 -5 -9 a5 5 0 0 1 5 -5 z" fill="var(--orange)"/><circle cx="15" cy="13" r="1.8" fill="var(--brown)"/></svg>
      <span>PO BOX 412 ASHFORD UT 84990</span>
    </div>
    <div class="contact-item">
      <svg width="30" height="30" viewBox="0 0 30 30"><circle cx="15" cy="15" r="14" fill="none" stroke="var(--orange)" stroke-width="1.5"/><rect x="9" y="10" width="12" height="9" rx="1" fill="none" stroke="var(--orange)" stroke-width="1.5"/><path d="M9 11 l6 5 l6 -5" fill="none" stroke="var(--orange)" stroke-width="1.5"/></svg>
      <span>office@heronvesselsinc.example</span>
    </div>
    <div class="contact-item">
      <svg width="30" height="30" viewBox="0 0 30 30"><circle cx="15" cy="15" r="14" fill="none" stroke="var(--orange)" stroke-width="1.5"/><path d="M10 9 l3 -1 l2 4 l-2 1.5 a8 8 0 0 0 3.5 3.5 l1.5 -2 l4 2 l-1 3 c-6 0 -11 -5 -11 -11 z" fill="var(--orange)"/></svg>
      <span>(555) 014-2290</span>
    </div>
    <div class="contact-item">
      <svg width="30" height="30" viewBox="0 0 30 30"><circle cx="15" cy="15" r="14" fill="none" stroke="var(--orange)" stroke-width="1.5"/><circle cx="15" cy="15" r="6.5" fill="none" stroke="var(--orange)" stroke-width="1.5"/><path d="M15 11 v4 h3" fill="none" stroke="var(--orange)" stroke-width="1.5"/></svg>
      <span>Mon - Fri 8 AM - 5PM MST</span>
    </div>
  </footer>
  <div class="flyer-foot"></div>
</main>
</body>
</html>
```